Velta Botanics Extension Remover

Remover Box
Same lingo on the back as we had before on the plastic pouch

Color pops
Will be sending info

Clips box
Will be sending info

Target Market(s)

Color pops
Will be sending info

Clips box
Will be sending info

Industry/Entity Type

Plastic

Requirements
Must have
• Same lingo on the back as we had before on the plastic pouch
• Color pops
• Will be sending info
• Clips box
• Will be sending info
Nice to have
• Color pops
• Will be sending info
• Clips box
• Will be sending info
Should not have
• Color pops
• Will be sending info
• Clips box
• Will be sending info

```html
<!DOCTYPE html>
<html lang="en">
<head>
<meta charset="utf-8">
<title>Velta Botanics Extension Remover</title>
<link rel="stylesheet" href="https://fonts.googleapis.com/css2?family=Didact+Gothic&display=swap">
<style>
  :root {
    --ink: #000000;
    --cream: #fbf1e3;
    --sand: #efe1d2;
    --peach: #f2c59c;
    --amber: #e8903a;
    --rust: #c2581f;
    --wine: #3f0c17;
    --berry: #6e1a2a;
    --rose: #a3384c;
    --skin: #f1cdb6;
    --skin-shade: #d9a287;
    --panel: rgba(255, 255, 255, 0.42);
  }
  * { margin: 0; padding: 0; box-sizing: border-box; }
  html, body {
    width: 927px;
    height: 1200px;
    overflow: hidden;
    background: #ffffff;
  }
  .package-front {
    position: relative;
    width: 927px;
    height: 1200px;
    overflow: hidden;
    font-family: "Didact Gothic", "Century Gothic", sans-serif;
    color: var(--ink);
  }
  .backdrop {
    position: absolute;
    inset: 0;
    background:
      radial-gradient(circle 220px at 210px 760px, rgba(232, 144, 58, 0.85) 0%, rgba(232, 144, 58, 0) 100%),
      radial-gradient(circle 180px at 90px 980px, rgba(194, 88, 31, 0.8) 0%, rgba(194, 88, 31, 0) 100%),
      radial-gradient(circle 260px at 260px 380px, var(--cream) 0%, rgba(251, 241, 227, 0) 100%),
      linear-gradient(180deg, var(--sand) 0%, #f3dcc4 35%, var(--peach) 60%, #e39a5c 85%, var(--rust) 100%);
  }
  .hero-photo {
    position: absolute;
    left: 452px;
    top: 0;
    width: 475px;
    height: 1200px;
    border-top-left-radius: 260px 340px;
    background:
      radial-gradient(ellipse 200px 140px at 250px 760px, rgba(241, 205, 182, 0.9) 0%, rgba(241, 205, 182, 0) 100%),
      linear-gradient(180deg,
        var(--wine) 0%,
        var(--berry) 22%,
        var(--rose) 42%,
        #c9746e 52%,
        var(--skin) 64%,
        var(--skin) 80%,
        var(--skin-shade) 92%,
        #b86f5c 100%);
  }
  .product-title {
    position: absolute;
    left: 26px;
    top: 1150px;
    width: 1110px;
    height: 66px;
    transform-origin: top left;
    transform: rotate(-90deg);
    font-size: 62px;
    font-weight: 400;
    line-height: 66px;
    white-space: nowrap;
    letter-spacing: 4.6px;
  }
  .label-panel {
    position: absolute;
    left: 112px;
    width: 324px;
    height: 213px;
    background: var(--panel);
    display: flex;
    align-items: center;
    justify-content: center;
    font-size: 39px;
  }
  .label-panel--color-pops { top: 97px; }
  .label-panel--clips-box { top: 934px; }
</style>
</head>
<body>
  <main class="package-front">
    <div class="backdrop"></div>
    <div class="hero-photo" role="img" aria-label="Photo of a woman with a curled burgundy updo and bright eye makeup, looking down, against a warm blurred background"></div>
    <h1 class="product-title">Velta Botanics Extension Remover</h1>
    <div class="label-panel label-panel--color-pops">Color pops</div>
    <div class="label-panel label-panel--clips-box">Clips Box</div>
  </main>
</body>
</html>
```